Design Business Cards for Corventa

We need new businesscards for our company called Corventa. The dimensions is 53mm x 85mm (widht x height), standing, not landscape. We want the businesscards to be creative and original.

On the front side, our company logo, see attached file.
On the backside: a personal photo, name, title, company name, adress, mobile, email and url. Instead of writing ex. "Email", feel free to us a symbol or icon.

Check these three links for inspiration for colours and design;
http://www.brightfold-samples.net/shop/demos/corventa/
http://www.brightfold-samples.net/shop/demos/corventa/activities.html
http://www.brightfold-samples.net/shop/demos/corventa/activity_details.html

```html
<!DOCTYPE html>
<html lang="en">
<head>
<meta charset="utf-8">
<title>Corventa Business Cards</title>
<link href="https://fonts.googleapis.com/css2?family=Lato:wght@400;700;900&display=swap" rel="stylesheet">
<style>
  :root {
    --page: #e4e4e4;
    --card: #ececec;
    --blue: #2f5a9e;
    --blue-deep: #244a86;
    --orange: #e0582a;
    --ink: #2b2b2b;
    --muted: #555;
    --white: #ffffff;
  }
  * { margin: 0; padding: 0; box-sizing: border-box; }
  html, body { width: 1200px; height: 899px; overflow: hidden; }
  body {
    background: var(--page);
    font-family: 'Lato', sans-serif;
    position: relative;
  }
  .card {
    position: absolute;
    width: 340px;
    height: 545px;
    background: var(--card);
    overflow: hidden;
    box-shadow: 0 6px 18px rgba(0,0,0,0.12);
  }
  .card-front { left: 215px; top: 177px; }
  .card-back { left: 645px; top: 177px; }
  .card-shapes { position: absolute; inset: 0; }

  .brand {
    position: absolute;
    display: flex;
    align-items: center;
    gap: 8px;
    white-space: nowrap;
  }
  .brand-dot {
    width: 22px; height: 22px;
    border-radius: 50%;
    background: var(--orange);
  }
  .brand-name {
    font-weight: 900;
    color: var(--blue);
    letter-spacing: 1px;
    text-transform: uppercase;
  }
  .card-front .brand { left: 34px; top: 70px; }
  .card-front .brand-name { font-size: 36px; }
  .card-back .brand { left: 128px; top: 38px; }
  .card-back .brand-dot { width: 14px; height: 14px; }
  .card-back .brand-name { font-size: 22px; }

  .scenery {
    position: absolute;
    left: 0; top: 225px;
    width: 340px; height: 270px;
    background: linear-gradient(160deg, #f1f1f1 0%, #d9dbdf 45%, #9fb2d2 70%, #e2e2e2 100%);
  }
  .tagline {
    position: absolute;
    left: 188px; top: 330px;
    font-size: 14px;
    line-height: 1.2;
    color: var(--ink);
    text-transform: uppercase;
    letter-spacing: 0.5px;
    white-space: nowrap;
  }
  .tagline strong { font-weight: 700; }

  .contact-icons {
    position: absolute;
    left: 46px; top: 150px;
    display: flex;
    flex-direction: column;
    gap: 14px;
  }
  .contact-icon { width: 30px; height: 30px; display: block; }

  .person { position: absolute; left: 140px; top: 80px; color: var(--ink); }
  .person-name { font-size: 15px; font-weight: 700; }
  .person-title { font-size: 10px; color: var(--muted); margin-bottom: 6px; }
  .person-line { font-size: 10px; line-height: 1.35; color: var(--ink); }
  .person-gap { height: 10px; }

  .portrait {
    position: absolute;
    left: 150px; top: 300px;
    width: 190px; height: 190px;
    background: linear-gradient(180deg, #e6e2df 0%, #c9b9ac 45%, #3a2e2a 75%, #23325e 100%);
  }
</style>
</head>
<body>

<section class="card card-front">
  <svg class="card-shapes" viewBox="0 0 340 545" width="340" height="545">
    <rect width="340" height="545" fill="var(--card)"/>
    <polygon points="170,200 340,160 340,200 150,225" fill="var(--orange)"/>
    <polygon points="0,215 200,185 170,205 0,235" fill="var(--blue)"/>
    <polygon points="0,530 340,495 340,510 0,545" fill="var(--orange)"/>
  </svg>
  <div class="brand"><span class="brand-dot"></span><span class="brand-name">Corventa</span></div>
  <div class="scenery" role="img" aria-label="Map of Norway in blue over a faint outdoor adventure photo"></div>
  <p class="tagline">Find <strong>Adventures</strong><br>All Across<br>Norway</p>
</section>

<section class="card card-back">
  <svg class="card-shapes" viewBox="0 0 340 545" width="340" height="545">
    <rect width="340" height="545" fill="var(--card)"/>
    <rect x="30" y="100" width="85" height="445" fill="var(--blue)"/>
    <polygon points="312,0 340,0 340,200 300,160" fill="var(--blue)"/>
    <polygon points="300,160 340,200 340,340 300,300" fill="var(--orange)"/>
    <polygon points="115,500 340,480 340,545 115,545" fill="var(--blue-deep)"/>
  </svg>
  <div class="brand"><span class="brand-dot"></span><span class="brand-name">Corventa</span></div>
  <div class="contact-icons">
    <svg class="contact-icon" viewBox="0 0 30 30"><circle cx="15" cy="15" r="13" fill="none" stroke="#fff" stroke-width="1.6"/><circle cx="15" cy="12" r="3.5" fill="#fff"/><path d="M8.5 21c1.5-3.5 11.5-3.5 13 0" fill="#fff"/></svg>
    <svg class="contact-icon" viewBox="0 0 30 30"><circle cx="15" cy="15" r="13" fill="none" stroke="#fff" stroke-width="1.6"/><path d="M11 9l2.5 3-1.5 1.5c1 2 2.5 3.5 4.5 4.5l1.5-1.5 3 2.5-1.5 2c-5 0-10-5-10-10z" fill="#fff"/></svg>
    <svg class="contact-icon" viewBox="0 0 30 30"><circle cx="15" cy="15" r="13" fill="none" stroke="#fff" stroke-width="1.6"/><path d="M8 15l14-6-5 13-2.5-5z" fill="#fff"/></svg>
    <svg class="contact-icon" viewBox="0 0 30 30"><circle cx="15" cy="15" r="13" fill="none" stroke="#fff" stroke-width="1.6"/><path d="M15 7a5 5 0 0 1 5 5c0 4-5 10-5 10s-5-6-5-10a5 5 0 0 1 5-5z" fill="#fff"/><circle cx="15" cy="12" r="1.8" fill="var(--blue)"/></svg>
  </div>
  <div class="person">
    <p class="person-name">Mira Halvorsen</p>
    <p class="person-title">Managing Director</p>
    <p class="person-line">+47 021-480-3315</p>
    <p class="person-line">+47 021-480-3315</p>
    <div class="person-gap"></div>
    <p class="person-line">post@corventa.no</p>
    <div class="person-gap"></div>
    <p class="person-line">Storgata 14,</p>
    <p class="person-line">Oslo 0155</p>
  </div>
  <div class="portrait" role="img" aria-label="Portrait photo of the managing director"></div>
</section>

</body>
</html>
```